Electrical Contracting business card design

We need a simple business card design for an Electrical Contracting business. A simple design would be appreciated
This company has 2 directors so on one it would have Dale Morrow & another with Shane Morrow.
Updates

Project Deadline Extended
Reason: Hello A few designers have asked for a logo unfortunately we don't have one so have extended deadline to see who can help us out with this. CHEERS

Project Deadline Extended
Reason: Waiting for business partner to return from xmas break. cheers

Industry/Entity Type

Business

Contact Information for Business Card

Quolvin Electrical Services P/L
REC: 63417
Residential Commercial Industrial
Service-Repairs-Renovations-Installations-Telephone-Data
Dale Morrow-Ph: 0437 612 388
Email: dale@quolvinelectrical.com.au

Requirements
Should not have
• The design should not have any electrical appliances in it ie: power-points, leads, houses etc.

```html
<!DOCTYPE html>
<html lang="en">
<head>
<meta charset="utf-8">
<title>Quolvin Electrical Services – Business Card</title>
<link rel="stylesheet" href="https://fonts.googleapis.com/css2?family=Oswald:wght@400;500;600&display=swap">
<style>
  :root {
    --backdrop: #3b4d4c;
    --card-white: #f7f7f5;
    --card-black: #151515;
    --ink: #1c1c1c;
    --amber: #d9a02b;
    --paper-text: #ffffff;
  }
  * { margin: 0; padding: 0; box-sizing: border-box; }
  html, body { width: 1200px; height: 1000px; overflow: hidden; }
  body {
    background: var(--backdrop);
    font-family: "Oswald", "Arial Narrow", sans-serif;
    display: flex;
    align-items: center;
    justify-content: center;
    gap: 60px;
  }
  .card {
    position: relative;
    width: 540px;
    height: 310px;
    overflow: hidden;
    box-shadow: 0 14px 30px rgba(0,0,0,.35);
  }
  /* front */
  .card--front { background: var(--card-white); color: var(--ink); }
  .front__band {
    position: absolute;
    left: 22px; top: 92px; bottom: 0;
    width: 86px;
    background: var(--card-black);
  }
  .front__mark {
    position: absolute;
    left: 14px; top: 80px;
    width: 102px; height: 102px;
    border-radius: 50%;
    background: var(--card-white);
    border: 6px solid var(--card-black);
    display: flex; align-items: center; justify-content: center;
    font-weight: 500; font-size: 17px; letter-spacing: .5px;
    color: var(--ink);
  }
  .front__title {
    position: absolute;
    left: 134px; top: 26px;
    font-weight: 600; font-size: 35px; letter-spacing: .3px;
    text-transform: uppercase; line-height: 1;
  }
  .front__person { position: absolute; left: 136px; top: 94px; }
  .person__name {
    font-weight: 500; font-size: 24px; color: var(--amber);
    text-transform: uppercase; line-height: 1;
  }
  .person__role { font-size: 12px; text-transform: uppercase; margin-top: 4px; }
  .contact { position: absolute; left: 136px; top: 156px; }
  .contact__row { display: flex; align-items: center; gap: 10px; margin-bottom: 5px; }
  .contact__label {
    width: 40px; height: 16px;
    background: var(--amber); color: var(--paper-text);
    font-size: 10px; text-transform: uppercase;
    display: flex; align-items: center; padding-left: 4px;
  }
  .contact__value { font-size: 12px; text-transform: uppercase; }
  .front__services {
    position: absolute; left: 136px; top: 222px; right: 24px;
    font-size: 11.5px; text-transform: uppercase; line-height: 1.55; letter-spacing: .2px;
  }
  /* back */
  .card--back {
    background: var(--card-black); color: var(--paper-text);
    display: flex; align-items: center; justify-content: center; gap: 16px;
  }
  .back__dot { width: 46px; height: 46px; border-radius: 50%; background: var(--amber); }
  .back__title {
    font-weight: 500; font-size: 34px; text-transform: uppercase; letter-spacing: .3px;
  }
</style>
</head>
<body>
  <section class="card card--front" aria-label="Card front">
    <div class="front__band"></div>
    <div class="front__mark">QUOLVIN</div>
    <h1 class="front__title">Quolvin Electrical Services</h1>
    <div class="front__person">
      <p class="person__name">Dale Morrow</p>
      <p class="person__role">Director</p>
    </div>
    <div class="contact">
      <div class="contact__row"><span class="contact__label">Tel</span><span class="contact__value">0437 612 388</span></div>
      <div class="contact__row"><span class="contact__label">Email</span><span class="contact__value">dale@quolvinelectrical.com.au</span></div>
    </div>
    <p class="front__services">
      Quolvin Electrical Services P/L REC : 63417<br>
      Residential Commercial Industrial Service<br>
      - Repairs - Renovations - Installations
    </p>
  </section>

  <section class="card card--back" aria-label="Card back">
    <span class="back__dot"></span>
    <p class="back__title">Quolvin Electrical Services</p>
  </section>
</body>
</html>
```